Torvane Interiors L.L.C

i need a brochure for y interior design company based in abu dhabi. the company was established in 2007 and is one of leading interior designing companies in Abu Dhabi. the company does variety of services starting from residential interior design, construction, furniture manufacturing and everything related to interior design from A-Z.
all our designs are made by our sister company ZELPHOR which is located at the same company but i do not wish to mention that in this brochure since i have a different brochure for zelphor. all pictures needed for the brochure can be taken from zelphor website (without the logo of course).

i want brief introduction about the company in the first page, and the team of work:

Torvane Interiors LLC was established in 2007 with a sole aim to cater to the interior design needs of the burgeoning housing industry and commercial advancement in the UAE.

We are an Abu Dhabi-based firm with a reputation for design excellence and budgetary responsibility. We were founded on the principle that a multi-disciplinary organization could respond with one clear vision to achieve clients' need for both functional efficiency and design excellence

Our Team

Today, our in-house team of architects, interior designers, engineers, and administrative teams continue to respond to each new challenge with technological expertise and innovative enthusiasm. The success of this approach is illustrated by the fact that more than 80 percent of our work is derived from satisfied repeat clients.

Torvane Interiors is distinguished by its diversity, simplicity, elegance and affordability. Our portfolio of projects demonstrates a variety of responses, all linked by a continuing commitment to inspire our clients and to exceed their expectations.

second page could be our services:
Our Services

We offer a wide range of services from planning, design consultancy, carpentry, furniture design and delivery of high end interiors. We mix textures, colors, ergonomics, experience and emotions. We strategize with the client to effectively blend lasting impact with bottom line budgets. We combine our client's tested values, culture and vision with our experience to create fresh, innovative and inspired spaces. We always stand out with our unique deigns by ZELPHOR and our furnishing textile by Weaver Quill.

3rd page
Residential:
(you could put few pictures of before and after or i can email some to you)

4th page:
commercial

5th page:
Retail

last page is contact page
Updates

what i want is an elegant glossy gold and black Multi purpose brochure which can be used as a blank brochure or as an A4 folder to submit quotations and other documents. so basically first page should have a photo of my own choice, but also if you open the folder in an A3 position it will have a full image of the image on the front page (so its basically half front half back kind of image).

on the inside, we will have a folded gold section down (to place a paper) on both sides right and left. on the left side, i want the Company's bio and the team.

on the right side is a glimpse of the projects (residential, commercial and retail)

all content can be taken from the website of zelphor and Lucien Marte Dubrais 

the last page (the back cover) should have our contact details which i will be posting shortly.

front image can be taken from the website of  Marte Dubrais  and if its not a good idea to put half front half back photo we can always put a full pic in the front and the same faded photo on the back.

the two pages inside could have a watermark of the logo in black on the entirely gold gloss paper with black font.

contact details are as the following:

Office #615
Noorwal Tower, Qasimat Street
Abu Dhabi
United Arab Emirates

Tel: +971-2-5550173
fax: +971-2-5550174
email: general enquiries: info@torvane-example.com
design: design@torvane-example.com
management: joulen@torvane-example.com
website: www.torvane-example.com

Industry/Entity Type

Residential

Font styles to use
Script

Colors
fee18a

Requirements
Must have
• full metalic gold with black imposing writing utside and full black inside

```html
<!DOCTYPE html>
<html lang="en">
<head>
<meta charset="utf-8">
<title>Torvane Interiors — Introduction &amp; Our Team</title>
<link rel="stylesheet" href="https://fonts.googleapis.com/css2?family=Varela+Round&display=swap">
<style>
  :root {
    --ink: #0b0b0b;
    --gold: #f1c500;
    --gold-line: #c9a400;
    --paper-text: #f4f4f4;
    --frame: #8a8a8a;
    --photo-dark: #3a3a3a;
    --photo-light: #9a9a9a;
    --swirl: #1c1c1c;
  }
  * { box-sizing: border-box; margin: 0; padding: 0; }
  html, body { width: 845px; height: 1200px; overflow: hidden; background: var(--ink); }
  .page {
    position: relative;
    width: 845px; height: 1200px;
    background: var(--ink);
    font-family: "Varela Round", Arial, sans-serif;
    color: var(--paper-text);
    overflow: hidden;
  }
  .swirl-decor {
    position: absolute; left: 0; top: 820px; width: 560px; height: 380px;
    background: radial-gradient(ellipse at 35% 55%, var(--swirl) 0%, rgba(28,28,28,0) 70%);
  }
  .section-title {
    position: absolute; left: 86px;
    font-size: 38px; font-weight: 700; color: var(--gold);
    letter-spacing: 0.5px;
    -webkit-text-stroke: 0.6px var(--gold);
  }
  .rule {
    position: absolute; left: 70px; width: 752px; height: 2px;
    background: var(--gold-line);
  }
  .body-copy {
    position: absolute; left: 76px; width: 736px;
    font-size: 17.6px; line-height: 30px;
    text-align: justify;
  }
  .team-photo {
    position: absolute; top: 470px; height: 190px;
    border: 3px solid var(--frame);
    background: linear-gradient(160deg, var(--photo-light), var(--photo-dark));
  }
  .team-caption {
    position: absolute; top: 664px; width: 200px;
    text-align: center; color: var(--gold);
    font-size: 13.5px; line-height: 18px; font-weight: 700;
  }
  .page-tab {
    position: absolute; left: 392px; top: 1112px; width: 52px; height: 88px;
    background: var(--gold);
  }
</style>
</head>
<body>
<main class="page">
  <div class="swirl-decor" role="img" aria-label="Faint dark floral swirl ornament"></div>

  <h1 class="section-title" style="top:82px;">Intoduction</h1>
  <div class="rule" style="top:126px;"></div>
  <p class="body-copy" style="top:142px;">Torvane Interiors LLC was established in 2007 with a sole aim to cater to the interior design needs of the burgeoning housing industry and commercial advancement in the UAE. We are an Abu Dhabi-based firm with a reputation for design excellence and budgetary responsibility. We were founded on the principle that a multi-disciplinary organization could respond with one clear vision to achieve clients' need for both functional efficiency and design excellence</p>
  <div class="rule" style="top:370px;"></div>

  <h2 class="section-title" style="top:404px;">Our Team</h2>
  <div class="rule" style="top:452px;"></div>

  <div class="team-photo" style="left:132px; width:166px;" role="img" aria-label="Black and white portrait of Joulen Haddar"></div>
  <div class="team-photo" style="left:312px; width:208px;" role="img" aria-label="Black and white portrait of Ilsa Varkonen"></div>
  <div class="team-photo" style="left:542px; width:174px;" role="img" aria-label="Black and white portrait of Tarek Nassim"></div>

  <p class="team-caption" style="left:115px;">Joulen Haddar<br>Sr. Interior Design Engineer</p>
  <p class="team-caption" style="left:316px;">Ilsa Varkonen<br>Sr. Designer</p>
  <p class="team-caption" style="left:529px;">Mr. Tarek Nassim<br>Projects Manager</p>

  <p class="body-copy" style="top:712px;">Today, our in-house team of architects, interior designers, engineers, and administrative teams continue to respond to each new challenge with technological expertise and innovative enthusiasm. The success of this approach is illustrated by the fact that more than 80 percent of our work is derived from satisfied repeat clients.</p>
  <p class="body-copy" style="top:884px;">Torvane Interiors is distinguished by its diversity, simplicity, elegance and affordability. Our portfolio of projects demonstrates a variety of responses, all linked by a continuing commitment to inspire our clients and to exceed their expectations.</p>

  <div class="page-tab"></div>
</main>
</body>
</html>
```